Advert for Services that we offer

Bolt Remova Ltd need an design to represent what we do in a modern way by showing an image with a brief description and the use of corporate logo the information we will proved vie a doc file and this is to be presented in a modern way. This design will be for print & web. we have done our own design and its not great i have put this in the file repository

Target Market(s)

Motor trade

Font styles to use
Sans Serif

Colors

Designer to choose colors to be used in the design.

Requirements
Must have
• Company colour scheme as per logo within the files uploaded.
• and a small boarder to isolate it from the rest of the articles.
Nice to have
• Modern font
Should not have
• Old style font

```html
<!DOCTYPE html>
<html lang="en">
<head>
<meta charset="utf-8">
<title>Bolt Remova Ltd – Product Testing and Analysis</title>
<link rel="stylesheet" href="https://fonts.googleapis.com/css2?family=Oswald:wght@500;600&family=Open+Sans:wght@600&display=swap">
<style>
  :root {
    --brand-blue: #1566b7;
    --brand-blue-dark: #0f4f93;
    --text-grey: #3b4049;
    --sky-light: #eaf6fd;
    --sky-mid: #9fd6f6;
    --sky-bright: #3fb0ef;
    --white: #ffffff;
    --photo-dark: #45484e;
    --photo-rust: #8a4a33;
  }
  html, body {
    margin: 0;
    padding: 0;
    width: 1200px;
    height: 775px;
    overflow: hidden;
    background: var(--white);
  }
  .advert {
    position: relative;
    width: 1200px;
    height: 775px;
    overflow: hidden;
    background:
      linear-gradient(115deg, transparent 55%, rgba(255,255,255,0.85) 80%, var(--white) 100%),
      linear-gradient(160deg, var(--sky-mid) 0%, var(--sky-light) 35%, var(--white) 55%, var(--sky-mid) 78%, var(--sky-bright) 100%);
    font-family: "Oswald", sans-serif;
  }
  .advert__photo {
    position: absolute;
    left: 0;
    top: 0;
    width: 230px;
    height: 775px;
    background: linear-gradient(180deg, var(--photo-dark) 0%, var(--photo-dark) 40%, var(--photo-rust) 100%);
  }
  .brand {
    position: absolute;
    left: 262px;
    top: 165px;
    width: 240px;
    display: flex;
    align-items: center;
    gap: 10px;
  }
  .brand__mark {
    width: 22px;
    height: 22px;
    background: var(--brand-blue);
    flex: none;
  }
  .brand__name {
    font-family: "Oswald", sans-serif;
    font-weight: 500;
    font-size: 30px;
    line-height: 1;
    color: var(--brand-blue);
    text-transform: uppercase;
    letter-spacing: 0.5px;
    white-space: nowrap;
  }
  .divider {
    position: absolute;
    left: 542px;
    top: 117px;
    width: 1px;
    height: 138px;
    background: var(--brand-blue);
  }
  .headline {
    position: absolute;
    left: 588px;
    top: 104px;
    margin: 0;
    font-family: "Oswald", sans-serif;
    font-weight: 600;
    font-size: 63px;
    line-height: 77px;
    color: var(--brand-blue);
    text-transform: uppercase;
    letter-spacing: 0;
  }
  .services {
    position: absolute;
    left: 600px;
    top: 279px;
    margin: 0;
    padding: 0;
    list-style: none;
  }
  .services__item {
    position: relative;
    padding-left: 26px;
    font-family: "Oswald", sans-serif;
    font-weight: 500;
    font-size: 33px;
    line-height: 54.5px;
    color: var(--text-grey);
    text-transform: uppercase;
    letter-spacing: 1px;
  }
  .services__item::before {
    content: "";
    position: absolute;
    left: 2px;
    top: 25px;
    width: 6px;
    height: 6px;
    border-radius: 50%;
    background: var(--text-grey);
  }
  .contact {
    position: absolute;
    left: 596px;
    top: 596px;
    width: 519px;
    height: 47px;
    box-sizing: border-box;
    border: 2px solid var(--brand-blue);
    border-radius: 24px;
    display: flex;
    align-items: center;
    font-family: "Open Sans", sans-serif;
    font-weight: 600;
    font-size: 19px;
    color: var(--brand-blue-dark);
  }
  .contact__web {
    padding-left: 26px;
    width: 282px;
  }
  .contact__sep {
    width: 1px;
    height: 22px;
    background: var(--brand-blue);
    margin-right: 30px;
  }
</style>
</head>
<body>
  <main class="advert">
    <div class="advert__photo" role="img" aria-label="Photo of a technician measuring the bore of a flanged cast housing with a digital dial gauge"></div>

    <div class="brand">
      <span class="brand__mark"></span>
      <span class="brand__name">Bolt Remova Ltd</span>
    </div>

    <div class="divider"></div>

    <h1 class="headline">Product Testing<br>and Analysis</h1>

    <ul class="services">
      <li class="services__item">Metallurgical Testing</li>
      <li class="services__item">Bearing Pre-Load Testing</li>
      <li class="services__item">Bore Measurement</li>
      <li class="services__item">New Product Evaluation</li>
      <li class="services__item">Product Analysis &amp; Report</li>
    </ul>

    <div class="contact">
      <span class="contact__web">www.bolt-remova.co.uk</span>
      <span class="contact__sep"></span>
      <span class="contact__phone">0161 555 0192</span>
    </div>
  </main>
</body>
</html>
```